Homepage for Travel NFT Marketplace

Hi there!
We are building a Travel Marketplace that incorporates NFTs. We are looking for a full page redesign of the homepage for this marketplace.
You can find the instructions along with all the content here at https://www.filquarry.com/sh/7xq2mvplet9wd4k/BBKrtuMzqWenHoxKfPcVa3ghd?dl=0
We look forward to seeing your submissions!
Industry/Entity Type
Tourism
Number of Pages Required
1 page
Font styles to use
Sans Serif
Colors
0094D4
00A9DD
6FCCEA
C7EBF8
E9F6FB
00AB8E
00BBA5
67D7C9
C6EFE9
E9F9F6
F0912C
F2A743
F7CA91
FBE8D2
FDF5EE
A7469A
B969AE
D3A5CF
EDDBEB
F8F0F9
6B429C
8869AF
B7A5CE
E3DAEB
F3F0F8
Requirements
Must have
- Clean, Modern & Fun!
Should not have
- Messy or Overcrowded

```html
<!DOCTYPE html>
<html lang="en">
<head>
<meta charset="utf-8">
<title>Coin Roamers – A New Way to Travel</title>
<link href="https://fonts.googleapis.com/css2?family=Nunito:wght@400;600;700;800&display=swap" rel="stylesheet">
<style>
:root{
  --navy:#0b1340;
  --navy-deep:#080f33;
  --band:#141c3d;
  --path:#18214f;
  --white:#ffffff;
  --muted:#b9bfd8;
  --pink:#e43bb6;
  --magenta:#c52fa6;
  --purple:#8869af;
  --violet:#6b429c;
  --blue:#3f7ee0;
  --cyan:#00a9dd;
  --sky:#6fccea;
}
*{margin:0;padding:0;box-sizing:border-box}
html,body{width:1200px;height:4068px;overflow:hidden}
body{font-family:'Nunito',sans-serif;background:var(--navy);color:var(--white);position:relative}
.abs{position:absolute}

/* header */
.site-header{position:absolute;left:0;top:0;width:1200px;height:74px;background:var(--white)}
.brand{position:absolute;left:95px;top:18px;display:flex;align-items:center;gap:10px;color:#1d1d3a;font-weight:600;font-size:17px}
.brand-dot{width:38px;height:38px;border-radius:50%;background:var(--magenta)}
.nav{position:absolute;top:28px;font-size:12px;font-weight:700;color:#1d1d3a;letter-spacing:.3px}
.nav-icon{position:absolute;top:19px;width:36px;height:36px;border-radius:50%;background:#f1e4f3}
.nav-icon i{position:absolute;left:11px;top:10px;width:14px;height:15px;border-radius:4px;background:var(--magenta)}

/* hero */
.hero{position:absolute;left:0;top:74px;width:1200px;height:637px;
  background:radial-gradient(ellipse 420px 360px at 0 40px,rgba(167,70,154,.55),transparent 70%),
             radial-gradient(ellipse 520px 420px at 830px 280px,rgba(40,70,170,.45),transparent 70%),
             var(--navy)}
.hero-title{position:absolute;left:122px;top:100px;font-size:64px;font-weight:700;line-height:76px}
.hero-title em{font-style:normal;color:var(--pink)}
.hero-sub{position:absolute;left:122px;top:262px;font-size:15px;line-height:27px;color:#e8e8f4;font-weight:600}
.btn{position:absolute;height:41px;border:2px solid var(--magenta);font-size:12px;font-weight:700;letter-spacing:.5px;
  display:flex;align-items:center;justify-content:center;color:var(--white);background:rgba(0,0,0,.1)}
.btn.ghost{border-color:#8e93b4}
.scroll-label{position:absolute;left:118px;top:455px;font-size:9px;letter-spacing:2px;color:#9aa0c0;writing-mode:vertical-rl;transform:rotate(180deg)}
.scroll-line{position:absolute;left:125px;top:500px;width:1px;height:60px;background:#3b4371}
.hub{position:absolute;left:742px;top:185px;width:184px;height:184px;border-radius:50%;background:var(--white);
  box-shadow:0 0 0 22px rgba(70,120,220,.25),0 0 60px 30px rgba(90,140,255,.45)}
.hub i{position:absolute;left:52px;top:52px;width:80px;height:80px;border-radius:50%;background:var(--magenta)}
.avatar{position:absolute;width:64px;height:64px;border-radius:50%;border:5px solid #1d2a66}
.photo{position:absolute;border-radius:3px}
.balloon{position:absolute;border-radius:50% 50% 45% 45%}

/* welcome */
.welcome{position:absolute;left:0;top:711px;width:1200px;height:216px;background:var(--band)}
.welcome h2{position:absolute;left:122px;top:62px;font-size:35px;font-weight:600;line-height:52px}
.welcome h2 span{color:var(--magenta);font-weight:700}
.welcome p{position:absolute;left:512px;font-size:15px;line-height:24px;color:#c7cbe0}
.more-link{position:absolute;left:930px;top:116px;display:flex;align-items:center;gap:9px;font-size:12px;font-weight:800;letter-spacing:.4px;border-bottom:2px solid var(--purple);padding-bottom:5px;padding-right:4px}
.more-link i{width:24px;height:24px;border-radius:50%;border:2px solid var(--magenta)}

/* features */
.features{position:absolute;left:0;top:927px;width:1200px;height:2073px;
  background:radial-gradient(ellipse 300px 600px at 1200px 200px,rgba(0,169,221,.3),transparent 70%),
             radial-gradient(ellipse 320px 500px at 1200px 1000px,rgba(167,70,154,.35),transparent 70%),
             radial-gradient(ellipse 500px 420px at 0 1300px,rgba(107,66,156,.35),transparent 70%),
             radial-gradient(ellipse 900px 260px at 600px 2073px,rgba(167,70,154,.55),transparent 75%),
             var(--navy)}
.section-title{position:absolute;left:0;width:1200px;text-align:center;font-size:34px;font-weight:600}
.section-title span{color:var(--blue);font-weight:700}
.num{position:absolute;width:64px;height:64px;border-radius:50%;background:linear-gradient(135deg,#3f7ee0,#a7469a);
  box-shadow:0 0 0 5px rgba(255,255,255,.9);font-size:36px;font-weight:800;display:flex;align-items:center;justify-content:center}
.feat h3{position:absolute;font-size:19px;font-weight:700}
.feat p{position:absolute;width:190px;font-size:12px;line-height:19px;color:#a9aecb}
.illus{position:absolute;border-radius:40%}
.big-heading{position:absolute;left:0;width:1200px;text-align:center;font-size:37px;font-weight:600;line-height:50px}
.big-heading span{color:var(--cyan)}
.ring-logo{position:absolute;left:556px;top:2637px;width:88px;height:88px;border-radius:50%;background:var(--white);border:6px solid #2e3a70}
.ring-logo i{position:absolute;left:18px;top:18px;width:40px;height:40px;border-radius:50%;background:var(--magenta)}

/* stats */
.stats{position:absolute;left:0;top:3000px;width:1200px;height:158px;background:linear-gradient(90deg,#1fb9e8,#6a7ad8 45%,#a24cb8 75%,#d22fa8)}
.stat-value{position:absolute;font-size:31px;font-weight:800}
.stat-label{position:absolute;font-size:14px;color:#eef0ff}
.stat-icon{position:absolute;width:28px;height:28px}

/* nft grid */
.nft{position:absolute;width:214px;height:214px}
.balloons-field{position:absolute;left:0;top:3774px;width:1200px;height:221px}

/* footer */
.footer{position:absolute;left:0;top:3995px;width:1200px;height:73px;background:linear-gradient(90deg,#1fb9e8,#6a7ad8 45%,#a24cb8 75%,#d22fa8)}
.footer small{position:absolute;top:29px;font-size:11px;color:#eef0ff}
.social{position:absolute;top:17px;width:38px;height:38px;border-radius:50%;border:1.5px solid rgba(255,255,255,.8)}
</style>
</head>
<body>

<header class="site-header">
  <div class="brand"><span class="brand-dot"></span>Coin Roamers</div>
  <span class="nav" style="left:692px">HOME</span>
  <span class="nav" style="left:757px">ABOUT</span>
  <span class="nav" style="left:829px">NFT</span>
  <span class="nav" style="left:880px">TRIPS</span>
  <span class="nav" style="left:944px">THE POT</span>
  <span class="nav-icon" style="left:1023px"><i style="border-radius:50%"></i></span>
  <span class="nav-icon" style="left:1068px"><i></i></span>
</header>

<section class="hero">
  <div class="balloon" role="img" aria-label="Hot air balloon illustration" style="left:30px;top:42px;width:58px;height:66px;background:linear-gradient(#c06a5a,#7d5fa8);opacity:.5"></div>
  <div class="balloon" role="img" aria-label="Hot air balloon illustration" style="left:328px;top:14px;width:34px;height:40px;background:linear-gradient(#e6a24b,#6b7fc9)"></div>
  <div class="balloon" role="img" aria-label="Hot air balloon illustration" style="left:945px;top:165px;width:32px;height:38px;background:linear-gradient(#e6a24b,#9b6bc9)"></div>

  <h1 class="hero-title">A New Way<br>to <em>Travel...</em></h1>
  <p class="hero-sub">Bridging The Gap Between Cryptocurrency &amp; Real<br>Life Adventures Like Never Before</p>
  <a class="btn" style="left:122px;top:349px;width:150px">LEARN MORE</a>
  <a class="btn ghost" style="left:281px;top:349px;width:150px">EXPLORE</a>
  <span class="scroll-label">SCROLL</span>
  <span class="scroll-line"></span>

  <svg class="abs" style="left:560px;top:60px" width="560" height="500" viewBox="0 0 560 500" fill="none" stroke="#4a5a9c" stroke-dasharray="4 5" stroke-width="1.5">
    <path d="M274 232 L95 110"/><path d="M274 232 L199 92"/><path d="M274 232 L350 90"/>
    <path d="M274 232 L454 111"/><path d="M274 232 L69 238"/><path d="M274 232 L481 238"/>
    <path d="M274 310 L72 455"/><path d="M274 310 L205 475"/><path d="M274 310 L340 475"/><path d="M274 310 L472 455"/>
  </svg>
  <div class="hub"><i></i></div>

  <div class="avatar" role="img" aria-label="NFT character avatar" style="left:624px;top:64px;background:#e2704f"></div>
  <div class="avatar" role="img" aria-label="NFT character avatar" style="left:727px;top:44px;background:#c9a6d8"></div>
  <div class="avatar" role="img" aria-label="NFT character avatar" style="left:878px;top:42px;background:#36c1a4"></div>
  <div class="avatar" role="img" aria-label="NFT character avatar" style="left:982px;top:64px;background:#13285e"></div>
  <div class="avatar" role="img" aria-label="NFT character avatar" style="left:597px;top:192px;background:#8fcbd4"></div>
  <div class="avatar" role="img" aria-label="NFT character avatar" style="left:1009px;top:192px;background:#f0b72c"></div>

  <div class="photo" role="img" aria-label="Photo of a traveller relaxing by a turquoise lagoon" style="left:573px;top:441px;width:117px;height:98px;background:linear-gradient(#3aa0a8,#2ab5c8 60%,#c99a78)"></div>
  <div class="photo" role="img" aria-label="Photo of a traveller at ancient rock-cut ruins" style="left:707px;top:461px;width:117px;height:98px;background:linear-gradient(#c98968,#8a5240)"></div>
  <div class="photo" role="img" aria-label="Photo of friends walking through a desert canyon" style="left:840px;top:461px;width:118px;height:98px;background:linear-gradient(#e8e2d8,#9c8a72)"></div>
  <div class="photo" role="img" aria-label="Photo of a woman in a red dress on a whitewashed island" style="left:974px;top:441px;width:117px;height:98px;background:linear-gradient(#5fa2e0,#e9eef5 60%,#c7414e)"></div>
</section>

<section class="welcome">
  <h2>Welcome to<br><span>Coin Roamers</span></h2>
  <p style="top:68px">The World's First Blockchain Travel Marketplace</p>
  <p style="top:106px">Our adventures are available exclusively<br>to those holding a certain NFT in their wallet</p>
  <a class="more-link"><i></i>MORE ABOUT US</a>
</section>

<section class="features">
  <h2 class="section-title" style="top:52px">What Sets <span>Us Apart?</span></h2>

  <svg class="abs" style="left:0;top:0" width="1200" height="2073" viewBox="0 0 1200 2073" fill="none">
    <path d="M608 128 V180 Q608 200 580 210 C470 250 455 320 470 390 C490 470 730 430 745 520 C760 620 490 630 485 715 C480 800 700 820 730 920 C760 1020 520 1000 515 1100 C510 1200 770 1230 780 1320 C790 1420 600 1420 600 1480 V1580"
      stroke="var(--path)" stroke-width="24" stroke-linecap="round"/>
    <path d="M570 1580 L630 1580 L600 1680 Z" fill="var(--path)"/>
  </svg>

  <div class="feat">
    <h3 style="left:231px;top:209px">The Adventures!</h3>
    <p style="left:231px;top:247px">We dig deep in our research &amp; work with local guides to create unique experiences not found anywhere else.</p>
    <div class="num" style="left:450px;top:211px">1</div>
    <div class="illus" role="img" aria-label="Illustration of a group of explorers hiking" style="left:616px;top:178px;width:252px;height:206px;background:radial-gradient(#3d5f7a,rgba(40,60,90,0) 70%)"></div>

    <h3 style="left:812px;top:449px">Intentional Travel</h3>
    <p style="left:814px;top:487px">We give you the ability to have a meaningful impact on local communities and offset the emissions from your travels.</p>
    <div class="num" style="left:707px;top:461px">2</div>
    <div class="illus" role="img" aria-label="Illustration of a marketplace screen floating on clouds" style="left:340px;top:439px;width:244px;height:189px;background:radial-gradient(#9fc9e6,rgba(60,90,130,0) 70%)"></div>

    <h3 style="left:231px;top:686px">Keep it Simple</h3>
    <p style="left:231px;top:727px">We dig deep in our research &amp; work with local guides to create unique experiences not found anywhere else.</p>
    <div class="num" style="left:451px;top:683px">3</div>
    <div class="illus" role="img" aria-label="Illustration of jungle leaves around a signpost" style="left:608px;top:652px;width:257px;height:182px;background:radial-gradient(#3a9a3a,rgba(40,80,50,0) 70%)"></div>

    <h3 style="left:812px;top:919px">Fellow Nomads</h3>
    <p style="left:814px;top:957px">We give you the ability to have a meaningful impact on local communities and offset the emissions from your travels.</p>
    <div class="num" style="left:718px;top:925px">5</div>
    <div class="illus" role="img" aria-label="Illustration of a classical temple framing a community page" style="left:316px;top:897px;width:276px;height:181px;background:radial-gradient(#c9a353,rgba(80,90,120,0) 70%)"></div>

    <h3 style="left:261px;top:1174px">Customer Experience</h3>
    <p style="left:261px;top:1213px">After booking a trip, all correspondence is done through our chat server, which is quick, easy and efficient.</p>
    <div class="num" style="left:487px;top:1171px">6</div>
    <div class="illus" role="img" aria-label="Illustration of gift boxes with confetti" style="left:624px;top:1094px;width:252px;height:190px;background:radial-gradient(#c25a9a,rgba(70,60,110,0) 70%)"></div>

    <h3 style="left:850px;top:1406px">Pure Crypto Baby!</h3>
    <p style="left:852px;top:1444px;width:220px">The world's first travel agency to exclusively accept cryptocurrencies. That's right, we're a crypto only zone... Sorry fiats, there's no room for you here!</p>
    <div class="num" style="left:754px;top:1413px">7</div>
    <div class="illus" role="img" aria-label="Illustration of a golden coin trophy on a pedestal" style="left:395px;top:1331px;width:213px;height:205px;background:radial-gradient(#d8a23c,rgba(70,80,110,0) 70%)"></div>
  </div>

  <h2 class="big-heading" style="top:1826px">Bridging The Gap between<br>Crypto &amp; <span>Real World Adventures</span></h2>
  <a class="btn" style="left:513px;top:1958px;width:172px">EXPLORE OUR NFTS</a>
</section>
<div class="ring-logo"><i></i></div>

<section class="stats">
  <span class="stat-value" style="left:231px;top:40px">$1,120,546</span>
  <span class="stat-label" style="left:231px;top:89px">Donated to Charity</span>

  <svg class="stat-icon" style="left:480px;top:46px" viewBox="0 0 28 28" fill="#fff"><rect x="3" y="11" width="22" height="6"/><rect x="5" y="17" width="18" height="10"/><rect x="12.5" y="8" width="3" height="19" fill="#6a7ad8"/><path d="M14 10 C8 2 4 8 10 10 Z M14 10 C20 2 24 8 18 10 Z"/></svg>
  <span class="stat-value" style="left:531px;top:43px">$456,060</span>
  <span class="stat-label" style="left:531px;top:92px">Given in Prizes to Our Community</span>

  <svg class="stat-icon" style="left:840px;top:46px" viewBox="0 0 28 28" fill="#fff"><path d="M10 3 L14 7 L18 3 L17 8 H11 Z"/><circle cx="14" cy="18" r="9"/><text x="14" y="22" font-size="11" text-anchor="middle" fill="#a24cb8" font-family="Nunito,sans-serif" font-weight="800">$</text></svg>
  <span class="stat-value" style="left:887px;top:43px">$56,060</span>
  <span class="stat-label" style="left:887px;top:92px">In the Adventure Pot</span>
</section>

<section class="nft-grid">
  <div class="nft" role="img" aria-label="NFT collectible character artwork" style="left:156px;top:3226px;background:radial-gradient(#d8c89a,#8a7440)"></div>
  <div class="nft" role="img" aria-label="NFT collectible character artwork" style="left:385px;top:3226px;background:radial-gradient(#8cc4e0,#2e6d8e)"></div>
  <div class="nft" role="img" aria-label="NFT collectible character artwork" style="left:613px;top:3226px;background:radial-gradient(#a487d8,#46308a)"></div>
  <div class="nft" role="img" aria-label="NFT collectible character artwork" style="left:842px;top:3226px;background:radial-gradient(#7fd06e,#2a7d3a)"></div>
  <div class="nft" role="img" aria-label="NFT collectible character artwork" style="left:156px;top:3455px;background:radial-gradient(#d07bb8,#7a2a6e)"></div>
  <div class="nft" role="img" aria-label="NFT collectible character artwork" style="left:385px;top:3455px;background:radial-gradient(#e27070,#8a1f2a)"></div>
  <div class="nft" role="img" aria-label="NFT collectible character artwork" style="left:613px;top:3455px;background:radial-gradient(#c9b058,#6a5a22)"></div>
  <div class="nft" role="img" aria-label="NFT collectible character artwork" style="left:842px;top:3455px;background:radial-gradient(#7fb8d8,#2a5e80)"></div>
  <a class="btn" style="left:513px;top:3720px;width:172px">EXPLORE OUR NFTS</a>
</section>

<div class="balloons-field" role="img" aria-label="Illustration of hot air balloons drifting across the night sky" style="background:radial-gradient(ellipse 600px 160px at 600px 221px,rgba(60,80,170,.35),transparent 75%)">
  <div class="balloon" style="left:62px;top:38px;width:70px;height:80px;background:linear-gradient(#d9a04c,#7e62b8)"></div>
  <div class="balloon" style="left:190px;top:0;width:40px;height:48px;background:#1c4aa8"></div>
  <div class="balloon" style="left:295px;top:90px;width:88px;height:100px;background:linear-gradient(#d9a04c,#7e62b8)"></div>
  <div class="balloon" style="left:475px;top:22px;width:42px;height:50px;background:#1c4aa8"></div>
  <div class="balloon" style="left:645px;top:42px;width:56px;height:64px;background:linear-gradient(#d9a04c,#7e62b8)"></div>
  <div class="balloon" style="left:585px;top:88px;width:38px;height:46px;background:linear-gradient(#d9a04c,#7e62b8)"></div>
  <div class="balloon" style="left:895px;top:105px;width:70px;height:80px;background:linear-gradient(#d9a04c,#7e62b8)"></div>
  <div class="balloon" style="left:966px;top:8px;width:40px;height:50px;background:#1c4aa8"></div>
  <div class="balloon" style="left:1118px;top:110px;width:48px;height:56px;background:linear-gradient(#d9a04c,#7e62b8)"></div>
</div>

<footer class="footer">
  <small style="left:122px">© 2022 Coin Roamers Inc. All Rights Reserved</small>
  <span class="social" aria-label="Social link" style="left:507px"></span>
  <span class="social" aria-label="Social link" style="left:556px"></span>
  <span class="social" aria-label="Social link" style="left:606px"></span>
  <span class="social" aria-label="Social link" style="left:655px"></span>
  <small style="left:872px">Terms &amp; Conditions</small>
  <small style="left:1006px">Privacy Policy</small>
</footer>

</body>
</html>
```